BrivoPeak Business Card Design Project

We are looking for a modern, clean business card design for our new company. We are a consulting firm focused on the financial services market providing management and IT consulting to banks, insurance companies, etc. Please include our company logo and company contact information from the attached file in the design. Two versions of the logo are attached, either version is acceptable. Logos are available in other file formats if needed. We would like to include the contact information for both our UK and US offices as well as the following information for each individual card holder: Name, position/title, address, phone number and e-mail address.
Updates
Project Deadline Extended
Reason: A last minute trip over seas has prevented us from finalizing the decision. A decision will be made this week. We apologize for the inconvenience.
Industry/Entity Type
Business
Contact Information for Business Card
Company logo.
Company locations and phone numbers for both the US and UK offices.
Company URL.
Cardholder Name
Cardholder Position/title
Cardholder Address
Cardholder Phone Number
Cardholder e-mail Address
Look and feel
Each slider illustrates characteristics of the customer's brand and the style your logo design should communicate.

```html
<!DOCTYPE html>
<html lang="en">
<head>
<meta charset="utf-8">
<title>BrivoPeak Partners – Business Card</title>
<link rel="stylesheet" href="https://fonts.googleapis.com/css2?family=Open+Sans:wght@400;600;700&display=swap">
<style>
  :root {
    --navy: #263d5f;
    --poly-light: #eceef0;
    --poly-mid: #d3d6da;
    --poly-dark: #bfc3c8;
    --white: #ffffff;
    --page: #e7e4df;
    --icon-bg: #e9ebee;
  }
  * { margin: 0; padding: 0; box-sizing: border-box; }
  html, body {
    width: 1200px; height: 1000px; overflow: hidden;
    background: var(--page);
    font-family: "Open Sans", Arial, sans-serif;
  }
  .card {
    position: absolute;
    width: 700px; height: 400px;
    left: 250px;
    overflow: hidden;
    box-shadow: 0 10px 30px rgba(0,0,0,0.22);
  }
  .card--front { top: 55px; background: var(--navy); }
  .card--back { top: 545px; }

  .poly-surface {
    position: absolute;
    background: linear-gradient(135deg, var(--poly-light) 0%, var(--poly-mid) 35%, var(--poly-light) 55%, var(--poly-dark) 80%, var(--poly-light) 100%);
  }
  .card--front .poly-surface { top: 0; right: 0; width: 205px; height: 100%; }
  .card--back .poly-surface { inset: 0; }

  .front-brand {
    position: absolute; top: 52px; right: 0; width: 205px;
    display: flex; flex-direction: column; align-items: center; gap: 2px;
    color: var(--navy);
  }
  .front-brand .brand-name { font-size: 24px; font-weight: 700; letter-spacing: -0.3px; }
  .front-brand .brand-sub { font-size: 10px; font-weight: 700; letter-spacing: 3px; }

  .holder { position: absolute; left: 48px; top: 78px; color: var(--white); }
  .holder-name { font-size: 30px; font-weight: 700; letter-spacing: 0.5px; line-height: 1.1; }
  .holder-title { font-size: 18px; font-weight: 400; margin-top: 2px; }

  .contact-list {
    position: absolute; left: 60px; top: 168px;
    list-style: none; color: var(--white);
    font-size: 13.5px; line-height: 1.32;
  }
  .contact-item { display: flex; gap: 12px; margin-bottom: 10px; }
  .contact-item .office + .office { margin-top: 10px; }
  .contact-icon {
    flex: none; width: 17px; height: 17px; margin-top: 2px;
    background: var(--icon-bg); border-radius: 2px;
    display: flex; align-items: center; justify-content: center;
  }
  .contact-icon svg { width: 11px; height: 11px; fill: var(--navy); }

  .back-band {
    position: absolute; left: 50%; top: 50%;
    width: 900px; height: 170px;
    transform: translate(-50%, -50%) rotate(-24deg);
    background: var(--navy);
    box-shadow: 0 6px 16px rgba(0,0,0,0.25);
    display: flex; align-items: center; justify-content: center;
  }
  .back-brand {
    display: flex; flex-direction: column; align-items: center;
    color: var(--white);
  }
  .back-brand .brand-name { font-size: 58px; font-weight: 700; letter-spacing: -0.5px; line-height: 1; }
  .back-brand .brand-sub { font-size: 18px; font-weight: 700; letter-spacing: 6px; margin-top: 6px; }
</style>
</head>
<body>

<section class="card card--front" aria-label="Business card front">
  <div class="poly-surface" role="img" aria-label="Light grey faceted low-poly texture"></div>
  <div class="front-brand">
    <span class="brand-name">BrivoPeak</span>
    <span class="brand-sub">PARTNERS</span>
  </div>

  <div class="holder">
    <p class="holder-name">YOUR NAME</p>
    <p class="holder-title">Designation</p>
  </div>

  <ul class="contact-list">
    <li class="contact-item">
      <span class="contact-icon"><svg viewBox="0 0 12 12"><path d="M6 0a4 4 0 0 0-4 4c0 3 4 8 4 8s4-5 4-8a4 4 0 0 0-4-4zm0 5.6A1.6 1.6 0 1 1 6 2.4a1.6 1.6 0 0 1 0 3.2z"/></svg></span>
      <div>
        <p class="office">418 N Cedar Ave, Suite 210-215<br>Fairmont UT 84120<br>United States</p>
        <p class="office">14-16 Halden Street<br>London<br>E2 4QX<br>Great Britain</p>
      </div>
    </li>
    <li class="contact-item">
      <span class="contact-icon"><svg viewBox="0 0 12 12"><path d="M2.4 0.6l2 2.2-1 1.4c.7 1.6 2 2.9 3.5 3.5l1.4-1 2.2 2-1.3 2.2C4.9 10.6 1.4 7.1.2 1.9z"/></svg></span>
      <p>US (801) 555-0147<br>UK +44 7700 900318</p>
    </li>
    <li class="contact-item">
      <span class="contact-icon"><svg viewBox="0 0 12 12"><path d="M6 0a6 6 0 1 0 0 12A6 6 0 0 0 6 0zm0 1.2c.6 0 1.3 1.3 1.6 3.2H4.4C4.7 2.5 5.4 1.2 6 1.2zM4.3 5.6h3.4a9 9 0 0 1 0 .8H4.3a9 9 0 0 1 0-.8zm-3 0h1.8v.8H1.3a4.8 4.8 0 0 1 0-.8zm7.6 0h1.8a4.8 4.8 0 0 1 0 .8H8.9zM4.4 7.6h3.2C7.3 9.5 6.6 10.8 6 10.8S4.7 9.5 4.4 7.6z"/></svg></span>
      <p>www.brivopeakpartners.com</p>
    </li>
  </ul>
</section>

<section class="card card--back" aria-label="Business card back">
  <div class="poly-surface" role="img" aria-label="Light grey faceted low-poly texture"></div>
  <div class="back-band">
    <div class="back-brand">
      <span class="brand-name">BrivoPeak</span>
      <span class="brand-sub">PARTNERS</span>
    </div>
  </div>
</section>

</body>
</html>
```